KTN Laredo Nuevo Artist Odette Pembrook event

Odette Pembrook

Elevate your appreciation for the arts with an Only-in-KTN VIP tour of the priceless art collection of El Paso's mysterious Odette, including access to her museum which is not open to the public. Dinner and transportation between sites included.

Odette Pembrook lives and works in El Paso, Texas. Praised by the Harbor Daily Courier as "fresh," "a tough act to follow," and the "ultimate in transgression," Pembrook is widely recognized in her home state of Texas as a unique presence and highly original artist. She has been characterized by Linda Fairweather, former curator at the Brightwater Gallery of Fine Works, as "an anachronism who earnestly pursues a long-held tradition of landscape and genre painting . . . inspired by her Southwestern environment and vivid imagination.

Rendered with thick applications of radiant colors, Pembrook's paintings are intensely personal, dream-like explorations of the natural world.
DATE: Wednesday, September 26, 2018
VENUE: RIO VISTA CIVIC TRUST HALL
518 W Calloway Ave
El Paso, TX 79947
United States
AGENDA: 6:00 - 7:30 Light supper and orientation to the mysterious Odette Pembrook, Rio Vista Civic Trust Hall downtown
7:30 - 7:45 Board van to go to Sagebrook Health Campus Odette Pembrook Chapel
7:45 - 8:15 View Chapel
8:15 - 8:30 Board van to go to Museum Pembrook
8:30 - 9:15 View Museum Pembrook with dessert
9:15 - 9:30 Return downtown
RESOURCE(S): Celia Wendt - Being an icon in the art world, and not needing any introduction, Celia probably knows more about Odette Pembrook than anyone!

Tomas Gable – President and CEO of the Rio Vista Civic Trust since 2011

Loranne Vega - Director of Presentations of the Odette Pembrook Museum and an art history graduate of SWCU

Neil Strauber - Nobody has ever actually seen Odette Pembrook, yet ophthalmologist and KTN member Dr. Neil Strauber is her eye surgeon. How can that be? Find out at the event!
ATTENDANCE: KTN Members, KTN Spouses/Guests, KTN SILVER Members, KTN SILVER Spouses/Guests
ATTIRE: Business Casual
DAY CHAIRS: Neil Strauber
Celia Wendt

Invite 5x7 or 7x5 please

Target Market(s)

KTN Laredo Nuevo Members

Industry/Entity Type

Non Profit

Font styles to use
Decorative
Script

Colors

Designer to choose colors to be used in the design.

Requirements
Must have
• Event title
• Date
• Artist description (Odette Pembrook)
• Venue
• Attire
• Attendees
• Logos
Nice to have
• Information about the artist
Should not have
• Art from another artists

```html
<!DOCTYPE html>
<html lang="en">
<head>
<meta charset="utf-8">
<title>KTN Laredo Nuevo – Odette Pembrook Invitation</title>
<link href="https://fonts.googleapis.com/css2?family=Anton&family=Archivo+Black&family=Cabin:wght@400;500;600&family=Oswald:wght@500;600&family=Tinos&display=swap" rel="stylesheet">
<style>
  :root{
    --ink:#000;
    --paper:#ecebe6;
    --gold:#d4a00c;
    --orange:#c2610c;
    --accent:#e0661a;
    --cream:#f3e7cf;
    --title-grey:#dcdcdc;
    --text:#f4f4f4;
    --band-ink:#1b1406;
  }
  *{box-sizing:border-box;margin:0;padding:0}
  html,body{width:1200px;height:1200px;overflow:hidden}
  body{background:var(--paper);position:relative;font-family:"Cabin",sans-serif}

  .card{position:absolute;width:728px;height:520px;background:var(--ink);overflow:hidden;box-shadow:0 4px 10px rgba(0,0,0,.25)}
  .card--front{left:68px;top:64px}
  .card--back{left:342px;top:602px}

  /* front */
  .title{position:absolute;left:0;top:0}
  .venue-name{position:absolute;left:0;width:728px;top:304px;text-align:center;font-family:"Archivo Black",sans-serif;font-size:24px;letter-spacing:1.5px;color:var(--title-grey)}
  .artist-bio{position:absolute;left:55px;top:344px;width:650px;font-size:10.4px;line-height:15.2px;color:var(--text);font-variant:small-caps;letter-spacing:.2px}
  .band{position:absolute;left:0;bottom:0;width:100%;height:72px;background:var(--gold)}
  .date-box{position:absolute;left:538px;top:410px;width:180px;height:110px;background:var(--orange);display:flex;justify-content:center;padding-top:20px}
  .date{font-family:"Oswald",sans-serif;font-weight:600;font-size:37px;line-height:1;color:var(--cream);white-space:nowrap}
  .address{font-family:"Oswald",sans-serif;font-weight:500;font-size:21px;line-height:1;color:var(--band-ink);position:absolute;white-space:nowrap}
  .card--front .address{left:50px;top:457px}
  .org{position:absolute;display:flex;align-items:center;gap:8px;color:var(--band-ink);line-height:1}
  .org__mark{width:12px;height:12px;background:var(--band-ink)}
  .org__name{font-family:"Tinos",serif;font-size:20px}
  .org__divider{width:1px;height:24px;background:var(--band-ink);margin:0 6px}
  .org__chapter{font-family:"Tinos",serif;font-size:17px}
  .card--front .org{left:50px;top:488px}

  /* back */
  .arcs{position:absolute;left:0;top:0}
  .side-rule{position:absolute;left:4px;top:13px;width:8px;height:408px;background:var(--orange)}
  .section-head{font-family:"Oswald",sans-serif;font-weight:600;color:var(--accent);font-size:23px;line-height:1}
  .agenda{position:absolute;left:40px;top:30px;width:460px}
  .agenda ul{list-style:none;margin-top:10px}
  .agenda li,.resources p,.detail__value{font-size:10px;line-height:15px;color:var(--text);font-variant:small-caps}
  .resources{position:absolute;left:40px;top:178px;width:660px}
  .resources .list{margin-top:11px}
  .resources p{line-height:15.8px}
  .resources .name{color:var(--accent)}
  .details{position:absolute;left:40px;top:340px;width:400px}
  .detail{display:flex;align-items:baseline;gap:14px}
  .detail .section-head{font-size:18px}
  .detail__value{font-size:10.5px}
  .detail--wrap .detail__value{max-width:300px}
  .details .section-head.solo{display:block;font-size:18px;margin-top:2px}
  .artwork{position:absolute;width:100px;height:88px}
  .card--back .org{left:40px;top:460px}
  .card--back .address{left:40px;top:489px;font-size:22px}
</style>
</head>
<body>

<section class="card card--front">
  <svg class="title" width="728" height="300" viewBox="0 0 728 300" role="img" aria-label="Artist name lettering filled with her golden painted artworks">
    <defs>
      <linearGradient id="paintGold" x1="0" y1="0" x2="1" y2="1">
        <stop offset="0" stop-color="#f1b21a"/>
        <stop offset=".3" stop-color="#c9620f"/>
        <stop offset=".55" stop-color="#f0c22e"/>
        <stop offset=".8" stop-color="#b7500d"/>
        <stop offset="1" stop-color="#e9a51d"/>
      </linearGradient>
    </defs>
    <text x="50" y="176" textLength="654" lengthAdjust="spacingAndGlyphs" font-family="Anton, sans-serif" font-size="184" fill="url(#paintGold)">ODETTE</text>
    <text x="55" y="296" textLength="626" lengthAdjust="spacingAndGlyphs" font-family="Anton, sans-serif" font-size="134" fill="url(#paintGold)">PEMBROOK</text>
  </svg>
  <h2 class="venue-name">RIO VISTA CIVIC TRUST HALL</h2>
  <p class="artist-bio">Odette Pembrook lives and works in El Paso, Texas. Praised by the Harbor Daily Courier as "fresh," "a tough act to follow," and the "ultimate in transgression," Pembrook is widely recognized in her home state of Texas as a unique presence and highly original artist. She has been characterized by Linda Fairweather, former curator at the Brightwater Gallery of Fine Works, as "an anachronism who earnestly pursues a long-held tradition of landscape and genre painting . . . inspired by her Southwestern environment and vivid imagination.</p>
  <div class="band"></div>
  <div class="date-box"><span class="date">9/26/2018</span></div>
  <p class="address">518 W Calloway Ave. El Paso, TX 79947 United States</p>
  <div class="org">
    <span class="org__mark"></span><span class="org__name">KTN</span>
    <span class="org__divider"></span><span class="org__chapter">Laredo Nuevo Chapter</span>
  </div>
</section>

<section class="card card--back">
  <svg class="arcs" width="728" height="520" viewBox="0 0 728 520" aria-hidden="true">
    <path d="M80 0 C 330 60, 470 260, 540 520 L 600 520 C 530 240, 380 40, 180 0 Z" fill="#ffffff" opacity=".12"/>
    <path d="M140 0 C 300 120, 380 320, 390 520" fill="none" stroke="#ffffff" stroke-width="30" opacity=".07"/>
  </svg>
  <div class="band"></div>
  <div class="side-rule"></div>

  <div class="agenda">
    <h3 class="section-head">AGENDA:</h3>
    <ul>
      <li>6:00 - 7:30 Light supper and orientation to the mysterious Odette Pembrook, Rio Vista Civic Trust Hall downtown</li>
      <li>7:30 - 7:45 Board van to go to Sagebrook Health Campus Odette Pembrook Chapel</li>
      <li>7:45 - 8:15 View Chapel</li>
      <li>8:15 - 8:30 Board van to go to Museum Pembrook</li>
      <li>8:30 - 9:15 View Museum Pembrook with dessert</li>
      <li>9:15 - 9:30 Return downtown</li>
    </ul>
  </div>

  <div class="resources">
    <h3 class="section-head">RESOURCE(S):</h3>
    <div class="list">
      <p><span class="name">Celia Wendt</span> - Being an icon in the art world, and not needing any introduction, Celia probably knows more about Odette Pembrook than anyone!</p>
      <p><span class="name">Tomas Gable</span> – President and CEO of the Rio Vista Civic Trust since 2011</p>
      <p><span class="name">Loranne Vega</span> - Director of Presentations of the Odette Pembrook Museum and an art history graduate of SWCU</p>
      <p><span class="name">Neil Strauber</span> - Nobody has ever actually seen Odette Pembrook, yet ophthalmologist and KTN member Dr. Neil Strauber is her eye surgeon. How can that be? Find out at the event!</p>
    </div>
  </div>

  <div class="details">
    <div class="detail detail--wrap"><span class="section-head">ATTENDANCE:</span><span class="detail__value">KTN Members, KTN Spouses/Guests, KTN SILVER Members, KTN SILVER Spouses/Guests</span></div>
    <div class="detail"><span class="section-head">ATTIRE:</span><span class="detail__value">Business Casual</span></div>
    <div class="detail"><span class="section-head">DAY CHAIRS:</span><span class="detail__value">Neil Strauber</span></div>
    <span class="section-head solo">Celia Wendt</span>
  </div>

  <div class="artwork" style="left:511px;top:1px;background:linear-gradient(135deg,#3b2a12,#e8c25a 50%,#2a3a1c)" role="img" aria-label="Painting of a radiant tree bursting with light"></div>
  <div class="artwork" style="left:619px;top:1px;background:radial-gradient(circle at 50% 40%,#ffd23a,#c8620f 70%,#7a2c08)" role="img" aria-label="Painting of a golden sunburst over hills"></div>
  <div class="artwork" style="left:511px;top:99px;background:linear-gradient(160deg,#f3c72a,#d48d12 60%,#a54b0c)" role="img" aria-label="Painting of swirling golden fields"></div>
  <div class="artwork" style="left:619px;top:99px;background:linear-gradient(180deg,#e9841b,#c4520c 60%,#5a2406)" role="img" aria-label="Painting of an orange desert landscape with figures"></div>
  <div class="artwork" style="left:511px;top:302px;background:linear-gradient(135deg,#c58a2a,#8a4e1c 50%,#d9b25a)" role="img" aria-label="Painting of a group gathered together"></div>
  <div class="artwork" style="left:619px;top:302px;background:linear-gradient(180deg,#d8501a,#f08a1c 60%,#7a2a0a)" role="img" aria-label="Painting of a town square at night"></div>
  <div class="artwork" style="left:511px;top:400px;background:linear-gradient(180deg,#c4782a,#3c3428 50%,#d8a23a)" role="img" aria-label="Painting of a dark stone in a golden field"></div>
  <div class="artwork" style="left:619px;top:400px;background:linear-gradient(135deg,#3b3a1a,#b8901e 50%,#2a2a12)" role="img" aria-label="Painting of desert plants at dusk"></div>

  <div class="org">
    <span class="org__mark"></span><span class="org__name">KTN</span>
    <span class="org__divider"></span><span class="org__chapter">Laredo Nuevo Chapter</span>
  </div>
  <p class="address">518 W Calloway Ave. El Paso, TX 79947 United States</p>
</section>

</body>
</html>
```